Clinician Harbor Collective

I am a financial planner whose client's are physicians and dentists. As physicians, there is very little time for them to do research on numerous aspects of their business and personal lives. I am looking to build a website that is a 1 stop shop for many of the services/resources they may need. It will be my job to screen the resources/advertisers and place competent people/business's that I know and have a track record on. there will ultimately be 10 or 12 ish areas that I would like to provide resources in:
disability insurance
life insurance
retirement planning
student loan advisors
employment contract and business formation attorneys
accountants
real estate agents
physician mortgages
personal loans
malpractice insurance
physician recruiters
maybe 2 other areas which I have yet to figure out.....
I would like each of these options to be able to be clicked on and a page will open up with the 1 or 2 or 3 or 4 people/business's that I have picked to represent these areas. I would like each specific person/business to have a click here to contact me link in which an email goes to the person and I am copied on the initial correspondence between the physician and the mortgage broker.... just so I can see some of the correspondence they will be receiving.
nowhere on the site do I want it to say my name. there will be certain disclosures that are needed and other wording but I think this is a good starting point.
here are links to two websites with the same general concept. please keep in mind that I want my website to be more on the simple side.
http://www.vantorelmedlink.example/index.html
http://bluestethwealth.example/
Industry/Entity Type
Financial

```html
<!DOCTYPE html>
<html lang="en">
<head>
<meta charset="utf-8">
<title>Clinician Harbor Collective</title>
<link rel="stylesheet" href="https://fonts.googleapis.com/css2?family=Exo+2:wght@300;400;500;700;800&family=Arimo:wght@400;700&display=swap">
<style>
  :root {
    --accent: #4ec1dc;
    --ink: #2f2f2f;
    --muted: #6a6a6a;
    --topbar: #f2f2f2;
    --band: #f8f8f8;
    --line: #d9d9d9;
    --footer: #333333;
    --white: #ffffff;
  }
  * { box-sizing: border-box; margin: 0; padding: 0; }
  html, body { width: 957px; height: 1200px; overflow: hidden; background: var(--white); }
  body { position: relative; font-family: "Arimo", Arial, sans-serif; color: var(--ink); }
  .abs { position: absolute; }

  .topbar { left: 0; top: 0; width: 957px; height: 20px; background: var(--topbar); font-size: 8px; }
  .topbar .social-dot { top: 6px; width: 7px; height: 7px; border-radius: 50%; background: #444; }
  .topbar .sep { top: 4px; width: 1px; height: 12px; background: var(--line); }
  .topbar .tlink { top: 5px; color: #444; }
  .topbar svg { top: 5px; }

  .header { left: 0; top: 20px; width: 957px; height: 46px; background: var(--white); border-bottom: 2px solid #e4e4e4; }
  .brand { left: 138px; top: 11px; font-family: "Exo 2", sans-serif; font-size: 16.5px; font-weight: 400; color: var(--ink); letter-spacing: 0.2px; }
  .nav a { position: absolute; top: 16px; font-size: 9.5px; color: var(--ink); text-decoration: none; font-family: "Exo 2", sans-serif; }
  .nav a.active { color: var(--accent); }

  .hero { left: 0; top: 66px; width: 957px; height: 187px;
    background: linear-gradient(180deg,
      #d8ecf3 0%, #b9dde9 22%,
      #3aa9b6 30%, #4db4bd 40%, #8fd0cf 50%,
      #e6e0d4 56%, #e9e2d6 70%, #ddd6ca 81%,
      #d4d3d0 82%, #ecebe8 92%, #f4f3f1 100%); }
  .hero-title { left: 138px; top: 51px; font-family: "Exo 2", sans-serif; font-weight: 800; font-size: 24.5px; color: #3a3a3a; letter-spacing: 0.9px; white-space: nowrap; }
  .hero-sub { left: 138px; top: 79px; font-family: "Exo 2", sans-serif; font-size: 14.5px; color: var(--white); white-space: nowrap; letter-spacing: 0.15px; }
  .btn { background: var(--accent); color: var(--white); font-size: 9.5px; text-align: center; letter-spacing: 0.6px; font-family: "Exo 2", sans-serif; }
  .hero .btn { left: 138px; top: 101px; width: 108px; height: 26px; line-height: 26px; }
  .hero .dot { top: 174px; width: 5px; height: 5px; border-radius: 50%; background: #9a9a9a; }
  .hero .dot.on { background: #333; }

  .welcome { left: 0; top: 273px; width: 957px; text-align: center; font-family: "Exo 2", sans-serif; }
  .welcome .w1 { font-size: 20px; font-weight: 300; letter-spacing: 0.6px; line-height: 22px; }
  .welcome .w2 { font-size: 20px; font-weight: 500; letter-spacing: 1px; line-height: 22px; }
  .welcome .rule { width: 80px; height: 2px; background: var(--accent); margin: 7px auto 8px; }
  .welcome .w3 { font-size: 8.5px; font-weight: 500; letter-spacing: 0.3px; }

  .card { width: 165px; height: 146px; }
  .card .photo { width: 165px; height: 105px; border: 1px solid #dcdcdc; }
  .card .title { position: absolute; left: 2px; top: 111px; width: 163px; font-size: 8.5px; font-family: "Exo 2", sans-serif; font-weight: 500; letter-spacing: 0.3px; }
  .card .title::after { content: "›"; position: absolute; right: 1px; top: -3px; font-size: 12px; }
  .card .desc { position: absolute; left: 2px; top: 123px; font-size: 7.7px; line-height: 7.2px; color: var(--muted); white-space: nowrap; }
  .card .rule { position: absolute; left: 0; top: 143px; width: 165px; height: 1.5px; background: var(--accent); }

  .features { left: 0; top: 877px; width: 957px; height: 123px; background: var(--band); border-top: 1px solid #ececec; border-bottom: 1px solid #ececec; }
  .feature { width: 146px; text-align: center; }
  .feature svg { display: block; margin: 0 auto; }
  .feature .name { font-family: "Exo 2", sans-serif; font-size: 12px; font-weight: 500; letter-spacing: 0.6px; margin-top: 7px; }
  .feature .desc { font-size: 7.7px; line-height: 7.2px; color: var(--muted); margin-top: 2px; white-space: nowrap; }
  .feature .rule { height: 1.5px; background: var(--accent); margin-top: 9px; }

  .heading { font-family: "Exo 2", sans-serif; font-size: 14.5px; font-weight: 500; letter-spacing: 0.6px; }
  .field { border: 1px solid #cfcfcf; background: var(--white); font-size: 7px; color: #777; padding: 4px 10px; letter-spacing: 0.3px; }
  .send { left: 381px; top: 1109px; width: 99px; height: 25px; line-height: 23px; border: 1px solid #2fa0bd; border-bottom-width: 3px; }
  .info-text { left: 523px; top: 1040px; width: 292px; font-size: 7.5px; line-height: 7.3px; color: #555; }
  .social-circle { top: 1093px; width: 21px; height: 16px; border-radius: 50%; }
  .location { left: 731px; top: 1073px; width: 89px; height: 61px; background: linear-gradient(135deg, #4a5056, #2b2f33); }
  .location span { position: absolute; left: 0; top: 34px; width: 89px; text-align: center; color: var(--white); font-family: "Exo 2", sans-serif; font-size: 12px; letter-spacing: 0.5px; }

  .footer { left: 0; top: 1154px; width: 957px; height: 46px; background: var(--footer); }
  .footer .copy { left: 138px; top: 18px; font-size: 9px; color: #bdbdbd; }
  .footer .mark { right: 139px; top: 13px; font-family: "Exo 2", sans-serif; font-size: 16px; font-weight: 300; color: #7a7a7a; letter-spacing: 0.3px; }
</style>
</head>
<body>

<div class="abs topbar">
  <div class="abs social-dot" style="left:137px"></div>
  <div class="abs social-dot" style="left:165px"></div>
  <div class="abs sep" style="left:184px"></div>
  <span class="abs tlink" style="left:196px">Log In</span>
  <div class="abs sep" style="left:232px"></div>
  <span class="abs tlink" style="left:246px">Sign Up</span>
  <svg class="abs" style="left:566px" width="10" height="10" viewBox="0 0 10 10"><path d="M2 1 L4 1 L5 3 L4 4 Q5 6 6 6 L7 5 L9 6 L9 8 Q8 9 6 8.5 Q2 7 1.2 3 Q1 1.6 2 1Z" fill="var(--accent)"/></svg>
  <span class="abs tlink" style="left:584px">0800-555-0142</span>
  <svg class="abs" style="left:689px;top:6px" width="14" height="9" viewBox="0 0 14 9"><rect width="14" height="9" rx="1" fill="var(--accent)"/><path d="M0.5 0.8 L7 5 L13.5 0.8" stroke="#fff" stroke-width="1" fill="none"/></svg>
  <span class="abs tlink" style="left:709px">ClinicianHarborCollective</span>
</div>

<header class="abs header">
  <div class="abs brand">Clinician Harbor Collective</div>
  <nav class="nav">
    <a class="active" style="left:507px" href="#">Home</a>
    <a style="left:575px" href="#">About</a>
    <a style="left:644px" href="#">Services</a>
    <a style="left:723px" href="#">Blog</a>
    <a style="left:785px" href="#">Contact</a>
  </nav>
</header>

<section class="abs hero" role="img" aria-label="Photo of an older couple riding bicycles along a beach boardwalk by the sea">
  <h1 class="abs hero-title">WE ARE THE FINANCIAL PLANNER !</h1>
  <p class="abs hero-sub">Lorem ipsum dolor sit amet, consectetu adipiscing elit, sed diam</p>
  <div class="abs btn">READ&nbsp; MORE</div>
  <div class="abs dot on" style="left:464px"></div>
  <div class="abs dot" style="left:476px"></div>
  <div class="abs dot" style="left:488px"></div>
</section>

<section class="abs welcome">
  <h2 class="w1">WELCOME TO THE</h2>
  <h2 class="w2">CLINICIAN HARBOR COLLECTIVE</h2>
  <div class="rule"></div>
  <p class="w3">CATAGORIES : CHOOSE YOUR OPTION !</p>
</section>

<!-- Row 1 -->
<div class="abs card" style="left:136px;top:363px"><div class="photo" role="img" aria-label="Photo of a caregiver with an elderly patient in a wheelchair" style="background:linear-gradient(120deg,#f1ede4 0%,#e2d6bf 45%,#b9a27c 80%,#8f7a58 100%)"></div><div class="title">DISABILITY INSURANCE</div><div class="desc">Lorem ipsum dolor sit amet, consectetu<br>adipiscing elit, sed diam</div><div class="rule"></div></div>
<div class="abs card" style="left:309px;top:363px"><div class="photo" role="img" aria-label="Photo of a team of doctors and nurses" style="background:linear-gradient(120deg,#f4f7f9 0%,#dfeaf2 45%,#8fc0dc 80%,#5e9fc7 100%)"></div><div class="title">LIFE INSURANCE</div><div class="desc">Lorem ipsum dolor sit amet, consectetu<br>adipiscing elit, sed diam</div><div class="rule"></div></div>
<div class="abs card" style="left:482px;top:363px"><div class="photo" role="img" aria-label="Photo of a couple meeting with a financial advisor" style="background:linear-gradient(120deg,#e9e1d6 0%,#c9b6a0 45%,#8f7560 80%,#5e4a3a 100%)"></div><div class="title">RETIREMENT PLANNING</div><div class="desc">Lorem ipsum dolor sit amet, consectetu<br>adipiscing elit, sed diam</div><div class="rule"></div></div>
<div class="abs card" style="left:655px;top:363px"><div class="photo" role="img" aria-label="Photo of a graduate in cap and gown with family" style="background:linear-gradient(120deg,#a89273 0%,#6e5f4b 40%,#2c2926 75%,#1c1b1a 100%)"></div><div class="title">STUDENT LOAN ADVISORS</div><div class="desc">Lorem ipsum dolor sit amet, consectetu<br>adipiscing elit, sed diam</div><div class="rule"></div></div>

<!-- Row 2 -->
<div class="abs card" style="left:136px;top:534px"><div class="photo" role="img" aria-label="Photo of business attorneys around a laptop" style="background:linear-gradient(120deg,#d8a772 0%,#a8784f 40%,#4a3c36 75%,#262224 100%)"></div><div class="title">BUSINESS&nbsp; ATTORNEYS</div><div class="desc">Lorem ipsum dolor sit amet, consectetu<br>adipiscing elit, sed diam</div><div class="rule"></div></div>
<div class="abs card" style="left:309px;top:534px"><div class="photo" role="img" aria-label="Photo of medical staff seated at a meeting table" style="background:linear-gradient(120deg,#f7f8f8 0%,#e7ecee 45%,#c4ced4 80%,#a6b3bb 100%)"></div><div class="title">PHYSICIAN RECRUITERS</div><div class="desc">Lorem ipsum dolor sit amet, consectetu<br>adipiscing elit, sed diam</div><div class="rule"></div></div>
<div class="abs card" style="left:482px;top:534px"><div class="photo" role="img" aria-label="Photo of a smiling group of doctors and nurses" style="background:linear-gradient(120deg,#eef3f6 0%,#bcd8ea 40%,#6ea9d2 75%,#3f82b6 100%)"></div><div class="title">MALPRACTICE INSURANCE</div><div class="desc">Lorem ipsum dolor sit amet, consectetu<br>adipiscing elit, sed diam</div><div class="rule"></div></div>
<div class="abs card" style="left:655px;top:534px"><div class="photo" role="img" aria-label="Photo of a delighted woman holding a fan of banknotes" style="background:linear-gradient(120deg,#f5efe9 0%,#e6cdb8 40%,#c59a7c 75%,#e9ece4 100%)"></div><div class="title">PERSONAL LOANS</div><div class="desc">Lorem ipsum dolor sit amet, consectetu<br>adipiscing elit, sed diam</div><div class="rule"></div></div>

<!-- Row 3 -->
<div class="abs card" style="left:136px;top:705px"><div class="photo" role="img" aria-label="Photo of a business handshake over documents" style="background:linear-gradient(120deg,#f0f0f0 0%,#c9c9cb 35%,#55575e 70%,#1f2026 100%)"></div><div class="title">EMPLOYMENT CONTRACT</div><div class="desc">Lorem ipsum dolor sit amet, consectetu<br>adipiscing elit, sed diam</div><div class="rule"></div></div>
<div class="abs card" style="left:309px;top:705px"><div class="photo" role="img" aria-label="Photo of two accountants reviewing a document" style="background:linear-gradient(120deg,#e9eff2 0%,#b7c9d3 40%,#7890a0 75%,#50606c 100%)"></div><div class="title">ACCOUNTANTS</div><div class="desc">Lorem ipsum dolor sit amet, consectetu<br>adipiscing elit, sed diam</div><div class="rule"></div></div>
<div class="abs card" style="left:482px;top:705px"><div class="photo" role="img" aria-label="Photo of a real estate agent handing keys to a couple" style="background:linear-gradient(120deg,#f4ede2 0%,#dfc9ad 40%,#b38c6c 75%,#d9dde2 100%)"></div><div class="title">REAL ESTATE AGENTS</div><div class="desc">Lorem ipsum dolor sit amet, consectetu<br>adipiscing elit, sed diam</div><div class="rule"></div></div>
<div class="abs card" style="left:655px;top:705px"><div class="photo" role="img" aria-label="Photo of a doctor and nurse reviewing a tablet" style="background:linear-gradient(120deg,#f2f5f7 0%,#d3e3ea 40%,#7fb5ca 75%,#4b93b0 100%)"></div><div class="title">PHYSICIAN MORTGAGES</div><div class="desc">Lorem ipsum dolor sit amet, consectetu<br>adipiscing elit, sed diam</div><div class="rule"></div></div>

<section class="abs features">
  <div class="abs feature" style="left:177px;top:16px">
    <svg width="46" height="40" viewBox="0 0 46 40">
      <circle cx="11" cy="6" r="5" fill="var(--accent)"/>
      <path d="M3 14 H20 V38 H3 Z" fill="var(--accent)"/>
      <path d="M28 10 L42 14 V24 Q42 34 28 39 Q14 34 14 24 V14 Z" fill="var(--accent)" stroke="#fff" stroke-width="2"/>
      <path d="M28 15 L37 18 V24 Q37 31 28 34 Z" fill="#fff" opacity="0.45"/>
    </svg>
    <div class="name">INSURANCE</div>
    <div class="desc">Lorem ipsum dolor sit amet, consectetu<br>adipiscing elit, sed diam</div>
    <div class="rule"></div>
  </div>
  <div class="abs feature" style="left:406px;top:16px">
    <svg width="52" height="40" viewBox="0 0 52 40">
      <rect x="2" y="26" width="7" height="13" fill="var(--accent)"/>
      <rect x="12" y="22" width="7" height="17" fill="var(--accent)"/>
      <rect x="22" y="18" width="7" height="21" fill="var(--accent)"/>
      <rect x="32" y="13" width="7" height="26" fill="var(--accent)"/>
      <rect x="42" y="8" width="7" height="31" fill="var(--accent)"/>
      <path d="M2 20 Q20 18 40 6" stroke="var(--accent)" stroke-width="3" fill="none"/>
      <path d="M36 2 L46 2 L42 11 Z" fill="var(--accent)"/>
    </svg>
    <div class="name">FINANCIAL</div>
    <div class="desc">Lorem ipsum dolor sit amet, consectetu<br>adipiscing elit, sed diam</div>
    <div class="rule"></div>
  </div>
  <div class="abs feature" style="left:634px;top:16px">
    <svg width="44" height="40" viewBox="0 0 44 40">
      <circle cx="22" cy="20" r="19" fill="var(--accent)"/>
      <circle cx="22" cy="20" r="13" fill="#fff"/>
      <circle cx="22" cy="20" r="9" fill="var(--accent)"/>
      <circle cx="22" cy="20" r="4" fill="#fff"/>
      <path d="M22 20 L38 6" stroke="#2f8fab" stroke-width="2.5"/>
      <path d="M36 3 L42 3 L39 9 Z" fill="#2f8fab"/>
    </svg>
    <div class="name">PLANNING</div>
    <div class="desc">Lorem ipsum dolor sit amet, consectetu<br>adipiscing elit, sed diam</div>
    <div class="rule"></div>
  </div>
</section>

<h3 class="abs heading" style="left:138px;top:1016px">CONTACT US</h3>
<div class="abs field" style="left:137px;top:1041px;width:169px;height:19px">NAME</div>
<div class="abs field" style="left:137px;top:1063px;width:169px;height:19px">EMAIL</div>
<div class="abs field" style="left:137px;top:1085px;width:169px;height:19px">PHONE NO.</div>
<div class="abs field" style="left:311px;top:1041px;width:169px;height:63px">MESSAGE</div>
<div class="abs btn send">SEND</div>

<h3 class="abs heading" style="left:523px;top:1016px">INFORMATION</h3>
<p class="abs info-text">Lorem ipsum dolor sit amet, consectetuer adipiscing elit, sed diam nonummy nibh euismod tincidunt ut laoreet dolore magna aliquam erat volutpat. Ut wisi enim ad minim veniam, quis nostrud exerci ...</p>
<h3 class="abs heading" style="left:523px;top:1067px">SOCIAL</h3>
<div class="abs social-circle" style="left:522px;background:#3b5a9a"></div>
<div class="abs social-circle" style="left:555px;background:#4aa3d8"></div>
<div class="abs social-circle" style="left:591px;background:#d9483b"></div>
<div class="abs social-circle" style="left:627px;background:#c8232c"></div>
<h3 class="abs heading" style="left:523px;top:1116px">KEEP IN TOUCH</h3>
<div class="abs location" role="img" aria-label="Small street map showing the office location">
  <svg class="abs" style="left:37px;top:14px" width="15" height="19" viewBox="0 0 15 19"><path d="M7.5 0 Q15 0 15 7.5 Q15 12 7.5 19 Q0 12 0 7.5 Q0 0 7.5 0Z" fill="var(--accent)"/><circle cx="7.5" cy="7" r="3" fill="#333"/></svg>
  <span>LOCATION</span>
</div>

<footer class="abs footer">
  <span class="abs copy">Clinician Harbor Collective © 2014.</span>
  <span class="abs mark">Clinician Harbor Collective</span>
</footer>

</body>
</html>
```